Dating Coach needs a Book Cover Design

My new book called "When to Turn the Tide: Meeting Romance Among the Endless Crowd of Digital Courtship" needs a cover! I tried to make one on my own, but it's just not my skill set :) Please see attached for my best attempt. I'd like to see the title smaller and the tagline bigger - so that the tagline is easier to read. But I'm not sure how to do this and still have the Title look great. I'm also considering if the "TURN THE TIDE" part should not be in all caps. Looking forward to your ideas! I'm also afraid that the drawing is a bit too cartoonish and doesn't match my brand. I'm looking for something elegant and also very approachable and down to earth. My website is www.petrawendtcoaching.example so you can use as reference! Please see my attached brand style guide for colors. This will be an e-book that I give away for free to anyone who signs up for my newsletter. Some mock-ups would also be great to use in advertising.

```html
<!DOCTYPE html>
<html lang="en">
<head>
<meta charset="utf-8">
<title>When to Turn the Tide — Book Cover</title>
<link rel="stylesheet" href="https://fonts.googleapis.com/css2?family=Cormorant+Garamond:wght@500&family=Playfair+Display:wght@400;500&family=Lora:wght@700&display=swap">
<style>
  :root {
    --page-bg: #eef0f2;
    --plum-deep: #2d1634;
    --plum-mid: #3b1d45;
    --plum-glow: #4c2659;
    --cream: #efe3cf;
    --cream-band: #e8dbc8;
    --ink-plum: #2a1232;
    --straw-light: #d8b878;
    --straw-mid: #b58f52;
    --straw-dark: #6e5228;
  }
  * { margin: 0; padding: 0; box-sizing: border-box; }
  html, body {
    width: 1200px; height: 1169px; overflow: hidden;
    background: var(--page-bg);
  }
  .cover {
    position: absolute; left: 220px; top: 44px;
    width: 760px; height: 1080px;
    background: var(--plum-deep);
    display: flex; flex-direction: column;
    box-shadow: 0 18px 40px rgba(0,0,0,0.18);
  }
  .cover__kicker {
    height: 166px;
    display: flex; align-items: center; justify-content: center;
    font-family: "Cormorant Garamond", serif;
    font-weight: 500; font-size: 52px;
    color: var(--cream);
    letter-spacing: 0.5px;
  }
  .cover__artwork {
    height: 360px;
    background:
      radial-gradient(ellipse at 45% 50%, var(--straw-light) 0%, var(--straw-mid) 55%, var(--straw-dark) 100%);
  }
  .cover__title {
    flex: 1;
    display: flex; flex-direction: column; align-items: center; justify-content: center;
    text-align: center;
    color: var(--cream);
    font-family: "Playfair Display", serif;
    background: radial-gradient(ellipse at 62% 80%, var(--plum-glow) 0%, var(--plum-mid) 40%, var(--plum-deep) 85%);
    padding-bottom: 8px;
  }
  .title__lead {
    font-weight: 400; font-size: 46px;
    letter-spacing: 12px; margin-right: -12px;
    line-height: 1;
  }
  .title__main {
    font-weight: 400; font-size: 118px;
    line-height: 1; margin-top: 12px;
    letter-spacing: -1px;
  }
  .title__bridge {
    font-weight: 400; font-size: 29px;
    line-height: 1; margin-top: 16px;
    letter-spacing: 0.5px;
  }
  .title__tail {
    font-weight: 500; font-size: 66px;
    line-height: 1; margin-top: 12px;
    letter-spacing: -1.5px;
  }
  .title__tail + .title__tail { margin-top: 4px; }
  .cover__author {
    height: 147px;
    background: var(--cream-band);
    display: flex; align-items: center; justify-content: center;
    font-family: "Lora", serif;
    font-weight: 700; font-size: 52px;
    color: var(--ink-plum);
  }
</style>
</head>
<body>
  <main class="cover">
    <p class="cover__kicker">When to Turn the Tide</p>
    <div class="cover__artwork" role="img" aria-label="Photograph of a pile of golden straw with a crumpled purple paper heart tucked among the stalks"></div>
    <h1 class="cover__title">
      <span class="title__lead">MEETING</span>
      <span class="title__main">ROMANCE</span>
      <span class="title__bridge">AMONG THE ENDLESS CROWD OF</span>
      <span class="title__tail">DIGITAL</span>
      <span class="title__tail">COURTSHIP</span>
    </h1>
    <p class="cover__author">Petra Wendt</p>
  </main>
</body>
</html>
```